Business Card Design

We have a group of different function companies owned and operated by one person. We are located in the Dallas Fort Worth area in Texas. We develop properties to where we are owners and develop properties that are not ours as well. We build custom homes and commercial buildings. We also do residential and commercial remodeling. We also own commercial properties in which we lease office space. We are trying to merge all we do into one card and have done so already into one website. We initially had thought of having a logo made with BC in nice attractive lettering maybe as a watermark. We are open to the color scheme but no neons or pastels.
Updates

Project Deadline Extended
Reason: I am needing 2 different cards for two businesses.

Industry/Entity Type

Residential

Contact Information for Business Card

Brambleton Companies
4186 Halvern Dr. Suite 417
Ashvale, Texas 75519
Land Development
Residential and Commercial Construction
Commercial Real Estate
Wade Pellingham
www.brambletonhq.example
wade@brambletonhq.example
Cell: 555-274-6183
Office: 555-609-7421
Fax: 5553918257

```html
<!DOCTYPE html>
<html lang="en">
<head>
<meta charset="utf-8">
<title>Brambleton Companies – Business Card</title>
<link rel="stylesheet" href="https://fonts.googleapis.com/css2?family=Carlito&family=Play&display=swap">
<style>
  :root {
    --brick: #85321f;
    --brick-text: #8a3a26;
    --panel: #e4cbc1;
    --ink: #111111;
    --card: #ffffff;
    --backdrop: #ece7e2;
  }
  * { margin: 0; padding: 0; box-sizing: border-box; }
  html, body { width: 1200px; height: 1000px; overflow: hidden; }
  body { background: var(--backdrop); position: relative; font-family: "Carlito", sans-serif; }

  .card {
    position: absolute; left: 275px; width: 650px; height: 380px;
    background: var(--card); overflow: hidden;
    box-shadow: 0 2px 8px rgba(0,0,0,0.18);
  }
  .card--front { top: 122px; }
  .card--back  { top: 555px; }

  .swoosh { position: absolute; inset: 0; }

  .brand-dot { position: absolute; border-radius: 50%; background: var(--brick); }
  .brand-name {
    position: absolute; font-family: "Play", sans-serif; font-weight: 400;
    color: var(--brick-text); white-space: nowrap; letter-spacing: 0.3px;
  }
  .card--front .brand-dot  { left: 68px; top: 118px; width: 76px; height: 76px; }
  .card--front .brand-name { left: 205px; top: 136px; font-size: 36px; }

  .card--back .brand-dot  { left: 88px; top: 82px; width: 56px; height: 56px; }
  .card--back .brand-name { right: 75px; top: 48px; font-size: 27px; }

  .address {
    position: absolute; left: 280px; width: 300px; top: 92px;
    text-align: center; font-size: 18px; line-height: 22px; color: var(--ink);
  }
  .address .web { color: var(--brick-text); font-family: "Play", sans-serif; font-size: 15px; }

  .services {
    position: absolute; left: 0; width: 650px; top: 206px;
    text-align: center; font-size: 15.5px; color: var(--ink);
  }

  .contact-panel {
    position: absolute; left: 30px; top: 262px; width: 588px; height: 74px;
    background: var(--panel); border-radius: 10px;
    display: flex; justify-content: space-between; padding: 7px 16px 0 22px;
    font-family: "Play", sans-serif; font-size: 16.5px; line-height: 21px; color: var(--brick-text);
  }
  .contact-panel .phones { text-align: right; }
</style>
</head>
<body>
  <section class="card card--front">
    <svg class="swoosh" width="650" height="380" viewBox="0 0 650 380" aria-hidden="true">
      <path d="M0 366 Q430 330 650 135 L650 380 L0 380 Z" fill="var(--brick)"/>
    </svg>
    <div class="brand-dot"></div>
    <div class="brand-name">Brambleton Companies</div>
  </section>

  <section class="card card--back">
    <div class="brand-dot"></div>
    <div class="brand-name">Brambleton Companies</div>
    <div class="address">
      <p>4186 Halvern Dr. Suite 417</p>
      <p>Ashvale, Texas 75519</p>
      <p class="web">www.brambletonhq.example</p>
    </div>
    <p class="services">Land Development · Residential &amp; Commercial Construction · Commercial Real</p>
    <div class="contact-panel">
      <div class="person">
        <p>Wade Pellingham</p>
        <p>President</p>
        <p>E-mail: wade@brambletonhq.example</p>
      </div>
      <div class="phones">
        <p>Cell: 555-274-6183</p>
        <p>Office: 555-609-7421</p>
        <p>Fax: 555-391-8257</p>
      </div>
    </div>
  </section>
</body>
</html>
```